Financial Services General Marketing Brochure

Need a brochure to help recipients understand what makes HLC unique and the services that we offer. Must match look/feel of website https://harborlanecustody.example Layouts should make it easy to read the content - content should not be crammed into a traditional size/layout. Please see attached creative brief for specifics.

Target Market(s)

Financial advisors and mature couples looking for trustee services.

Industry/Entity Type

Financial Service

Colors
34a7d8
ffc214

Requirements
Must have
• See Creative Brief

```html
<!DOCTYPE html>
<html lang="en">
<head>
<meta charset="utf-8">
<title>HLC Brochure – Inside Spread</title>
<link href="https://fonts.googleapis.com/css2?family=Open+Sans:wght@400;600;700&family=Source+Serif+4:ital,wght@0,400;0,600;1,400&display=swap" rel="stylesheet">
<style>
  :root{
    --navy:#3f5a75;
    --steel:#547491;
    --body:#5a5a5a;
    --gold:#f0b743;
    --gold-deep:#e9ab2e;
    --cream:#f8f2ec;
    --ring:#d6c2aa;
    --ring-fill:#fffdf8;
    --paper:#ffffff;
    --rule:#cfcfcf;
  }
  *{margin:0;padding:0;box-sizing:border-box}
  html,body{width:1200px;height:998px;overflow:hidden;background:var(--paper)}
  body{position:relative;font-family:"Open Sans",sans-serif;color:var(--body)}
  .spread{position:absolute;left:0;top:200px;width:1200px;height:600px;border:1px solid var(--rule)}
  .fold{position:absolute;left:600px;top:180px;height:640px;border-left:2px dashed #cfcfcf}
  .portrait{position:absolute;left:1px;top:1px;width:299px;height:165px;
    background:linear-gradient(135deg,#5d5a52 0%,#8a8172 40%,#3c4a66 75%,#2b3b5a 100%)}
  .letter{position:absolute;left:42px;top:203px;width:222px;font-size:11.2px;line-height:17.4px;letter-spacing:.45px}
  .letter p+p{margin-top:17.4px}
  .dropcap{float:left;font-family:"Source Serif 4",serif;font-size:62px;line-height:50px;color:var(--steel);margin:3px 4px 0 0}
  .signature{position:absolute;left:94px;top:535px;font-size:12.5px;line-height:18px}
  .signature strong{font-weight:600;color:#444}
  .band{position:absolute;top:34px;height:66px;display:flex;flex-direction:column;justify-content:center;align-items:center;color:#fff;font-family:"Source Serif 4",serif}
  .band--unique{left:300px;width:300px;background:var(--steel);font-size:21px;letter-spacing:.3px}
  .features{position:absolute;left:325px;top:131px;width:250px}
  .feature h3{font-family:"Source Serif 4",serif;font-style:italic;font-weight:400;font-size:15px;color:var(--steel);margin-bottom:6px}
  .feature p{font-size:10.4px;line-height:14.8px;letter-spacing:.15px}
  .feature+.feature{margin-top:14px}
  .team{position:absolute;left:600px;top:0;width:599px;height:598px;background:var(--cream)}
  .band--team{left:0;width:599px;background:linear-gradient(90deg,var(--gold-deep),var(--gold) 50%,var(--gold-deep))}
  .band--team .inner{display:flex;flex-direction:column;align-items:center;margin-left:-16px}
  .band--team .sub{font-family:"Open Sans",sans-serif;font-size:17px;letter-spacing:.5px;opacity:.95}
  .band--team .title{font-size:21px;letter-spacing:.4px}
  .diagram{position:absolute;left:0;top:0}
  .role{font-family:"Open Sans",sans-serif;font-weight:700;fill:var(--navy)}
  .tag{font-family:"Open Sans",sans-serif;font-weight:600;font-size:7.5px;fill:#fff}
  .small{font-family:"Source Serif 4",serif;font-size:6px;fill:var(--navy)}
</style>
</head>
<body>
<div class="fold"></div>
<section class="spread">
  <div class="portrait" role="img" aria-label="Portrait photo of the founding principal in a blue suit in an office"></div>
  <div class="letter">
    <p><span class="dropcap">W</span>e understand that wealth and families is very complex. As families try to transfer wealth it can be an incredible blessing or, if done improperly, can be incredibly destructive. Often a neutral third party is needed to come alongside the family’s advisory team to provide guidance as families go through their wealth transition.</p>
    <p>Our relational focus, and Open Harbor approach, helps families to successfully navigate through the complexities of wealth, family and trusts. We believe a family “legacy” is about more than just money.</p>
  </div>
  <div class="signature"><strong>Daniel Hartley, J.D.</strong><br>Founding Principal</div>

  <div class="band band--unique">What Makes HLC Unique</div>
  <div class="features">
    <div class="feature"><h3>Responsive</h3><p>The family deals directly with decision makers instead of being subject to committees with whom the family may never have the opportunity to interact or engage.</p></div>
    <div class="feature"><h3>Family Focus</h3><p>We help families successfully navigate the complexities of family wealth, not just perform trust administration.</p></div>
    <div class="feature"><h3>Independent</h3><p>To avoid any conflicts of interest, we have no formal affiliations with wealth management firms or financial advisory practices.</p></div>
    <div class="feature"><h3>Customized</h3><p>Together we develop a customized approach that will best suit the family's needs.</p></div>
    <div class="feature"><h3>Collaborative</h3><p>We work collaboratively with the family's team of trusted professionals.</p></div>
  </div>

  <div class="team">
    <div class="band band--team"><div class="inner"><span class="sub">Harbor Lane Custody</span><span class="title">Client/Family Centered Team</span></div></div>
    <svg class="diagram" width="599" height="598" viewBox="0 0 599 598">
      <g stroke="var(--ring)" stroke-width="4">
        <line x1="188" y1="310" x2="210" y2="310"/><line x1="400" y1="310" x2="416" y2="310"/>
        <line x1="240" y1="390" x2="230" y2="400"/><line x1="360" y1="390" x2="372" y2="400"/>
      </g>
      <g fill="var(--ring-fill)" stroke="var(--ring)" stroke-width="3">
        <circle cx="130" cy="310" r="58"/><circle cx="474" cy="310" r="58"/>
        <circle cx="206" cy="440" r="58"/><circle cx="406" cy="443" r="58"/>
        <circle cx="309" cy="521" r="58"/>
      </g>
      <circle cx="229" cy="180" r="62" fill="#8a7a63" stroke="var(--ring)" stroke-width="3" role="img" aria-label="Photo of a smiling woman, the current beneficiary"/>
      <circle cx="376" cy="180" r="58" fill="#e6d3c4" stroke="var(--ring)" stroke-width="3" role="img" aria-label="Photo of two young children, the future beneficiaries"/>
      <polygon points="256,232 356,232 404,310 356,388 256,388 208,310" fill="#d9cfc4" stroke="#efe3d3" stroke-width="2" role="img" aria-label="Photo of a smiling older couple, the trust creators"/>
      <text class="tag" x="230" y="222" text-anchor="middle">Current Beneficiary</text>
      <text class="tag" x="377" y="222" text-anchor="middle" style="fill:var(--navy)">Future Beneficiary</text>
      <text class="role" x="305" y="382" text-anchor="middle" font-size="12.5">Trust Creator</text>
      <text class="role" x="130" y="314" text-anchor="middle" font-size="14">Attorney</text>
      <text class="role" x="474" y="314" text-anchor="middle" font-size="14">Accountant</text>
      <text class="role" x="206" y="445" text-anchor="middle" font-size="14">Financial</text>
      <text class="role" x="406" y="448" text-anchor="middle" font-size="14">Trustee</text>
      <text class="role" x="309" y="508" text-anchor="middle" font-size="12">Human Capital</text>
      <text class="role" x="309" y="523" text-anchor="middle" font-size="12">Resources</text>
      <text class="small" x="312" y="537" text-anchor="middle">Legacy Development</text>
      <text class="small" x="312" y="546" text-anchor="middle">Health Care Management</text>
      <text class="small" x="312" y="555" text-anchor="middle">Philanthropic Services</text>
      <text class="small" x="312" y="564" text-anchor="middle">Life Coaching</text>
    </svg>
  </div>
</section>
</body>
</html>
```